Business cards for Tile Contractor
Brisk Grout Studio
LAST MINUTE ADDITION TO BUSINESS CARD!!
website address: briskgroutstudio.net
and a space after the area code in phone number:
thanks!!
#85 is closest to what im looking for. Thanks for all the drafts! good stuff!
looks good so far. would like to see more with all the info on the card.

```html
<!DOCTYPE html>
<html lang="en">
<head>
<meta charset="utf-8">
<title>Brisk Grout Studio — Business Card</title>
<link href="https://fonts.googleapis.com/css2?family=Open+Sans:wght@400;600;700&display=swap" rel="stylesheet">
<style>
  :root {
    --page-bg: #eef0f2;
    --card-white: #ffffff;
    --navy-deep: #0a2350;
    --navy-mid: #123a78;
    --blue-glow: #1e7fc4;
    --band-grey: #8f949b;
    --band-grey-light: #c4c8cd;
    --logo-navy: #1b3566;
    --text-light: #ffffff;
    --faint: #e8ebef;
  }
  * { margin: 0; padding: 0; box-sizing: border-box; }
  html, body {
    width: 1200px; height: 935px; overflow: hidden;
    background: var(--page-bg);
    font-family: "Open Sans", Arial, sans-serif;
  }
  .canvas { position: relative; width: 1200px; height: 935px; }
  .business-card {
    position: absolute; left: 100px; top: 182px;
    width: 1000px; height: 571px;
    border-radius: 36px; overflow: hidden;
    background: var(--card-white);
    box-shadow: 0 10px 28px rgba(0,0,0,0.18);
  }
  .card-shapes { position: absolute; inset: 0; }
  .owner { position: absolute; left: 54px; top: 72px; color: var(--text-light); }
  .owner-name { font-size: 32px; font-weight: 700; line-height: 1.2; }
  .owner-title { font-size: 19px; font-weight: 600; margin-top: 6px; }
  .contact {
    position: absolute; left: 54px; top: 362px;
    color: var(--text-light); font-size: 21px; line-height: 1.55;
    list-style: none;
  }
  .contact .street { font-weight: 600; }
  .brand {
    position: absolute; left: 540px; top: 98px;
    display: flex; align-items: center; gap: 16px;
  }
  .brand-dot { width: 60px; height: 60px; border-radius: 50%; background: var(--logo-navy); }
  .brand-name { font-size: 35px; font-weight: 700; color: var(--logo-navy); letter-spacing: 0.3px; }
  .faint-mark {
    position: absolute; left: 735px; top: 270px;
    width: 170px; height: 170px; border-radius: 50%;
    background: var(--faint);
  }
</style>
</head>
<body>
<main class="canvas">
  <article class="business-card">
    <svg class="card-shapes" viewBox="0 0 1000 571" width="1000" height="571" aria-hidden="true">
      <defs>
        <radialGradient id="blueField" cx="0.33" cy="0.55" r="0.65">
          <stop offset="0" stop-color="var(--blue-glow)"/>
          <stop offset="0.55" stop-color="var(--navy-mid)"/>
          <stop offset="1" stop-color="var(--navy-deep)"/>
        </radialGradient>
        <linearGradient id="greyBand" x1="0" y1="0" x2="1" y2="1">
          <stop offset="0" stop-color="var(--band-grey)"/>
          <stop offset="1" stop-color="var(--band-grey-light)"/>
        </linearGradient>
      </defs>
      <path d="M0,0 H345 C385,0 410,150 480,300 C545,440 610,530 700,571 H0 Z" fill="url(#greyBand)"/>
      <path d="M0,0 H300 C340,0 365,150 435,300 C500,445 560,535 650,571 H0 Z" fill="url(#blueField)"/>
    </svg>

    <header class="owner">
      <p class="owner-name">Zandu Reyes</p>
      <p class="owner-title">Owner/Tile Setter</p>
    </header>

    <ul class="contact">
      <li class="street">418 E. Marlow St.</li>
      <li class="street">Ventura, Ca 93001</li>
      <li>Phone: (805) 555-0147</li>
      <li>Email : briskgroutstudio@ymail.com</li>
      <li>Web : briskgroutstudio.net</li>
    </ul>

    <div class="brand">
      <span class="brand-dot"></span>
      <span class="brand-name">Brisk Grout Studio</span>
    </div>

    <div class="faint-mark" aria-hidden="true"></div>
  </article>
</main>
</body>
</html>
```